Kestrelwood Pathways Agency business cards

Australian company about to start offering its services. We recruit international students to come to study English, vocational education and postgraduate courses in Australia. We help them find the institution and select the right city they want to come to Australia. We are a young, online oriented and supportive agency. Our clients are between 18 and 35 years old, mainly University students, young professionals or people with work experience. We provide much more information that any other agency offer. We administrate a Facebook group with more than 11.000 members that daily ask questions about general information when coming to Australia, while they are here and even after they leave the country

Target Market(s)

International students from South America, Central America and Europe

Industry/Entity Type

Student

Contact Information for Business Card

Tomas Brevik
Managing Director
tomas@velmorin.com.au
www.velmorin.com.au
+61 491058263
Melbourne, Australia

Font styles to use
Serif
Sans Serif

Colors

Designer to choose colors to be used in the design.

Requirements
Must have
• Horizontal design
• Standard business card size and shape. If font uses green or yellow colours, they will have to match the ones from the logo
Nice to have
• UPDATE: Use the contents of the green image to design one of the card sides. Use our logo in the background of that side as watermark.
• Passport image, or immigration stamps. A picture of the Yarra River (from Melbourne) would be cool as well.
Should not have
• Non-standard business card size and shape
• Not black as the background colour of any sides as we are not a VIP agency or a hight class service. We are orientes to young people and they like colours, pictures, something attractive.
• Vertical design
• NO YELLOW or BLACK AS THE BACKGROUND COLOUR OF ANY SIDE OF THE BIZ CARD

```html
<!DOCTYPE html>
<html lang="en">
<head>
<meta charset="utf-8">
<title>Kestrelwood Pathways Agency – Business Cards</title>
<link href="https://fonts.googleapis.com/css2?family=Jost:wght@400;500;600&display=swap" rel="stylesheet">
<style>
  :root {
    --stage: #d9dde2;
    --card: #173a5c;
    --green: #2f9d5c;
    --yellow: #f2c21b;
    --white: #f4f4f4;
    --silver: #d2d8de;
    --tagline: #8fa6bf;
  }
  * { margin: 0; padding: 0; box-sizing: border-box; }
  html, body {
    width: 1200px; height: 900px; overflow: hidden;
    background: var(--stage);
    font-family: "Jost", "Futura", sans-serif;
  }
  .stage {
    width: 1200px; height: 900px;
    display: flex; flex-direction: column;
    align-items: center; justify-content: center; gap: 40px;
  }
  .card {
    width: 700px; height: 380px;
    background: var(--card);
    box-shadow: 0 12px 26px rgba(0,0,0,0.25);
    position: relative;
  }
  /* Back side */
  .card--back {
    display: flex; flex-direction: column;
    align-items: center; justify-content: center;
  }
  .card--back .wordmark {
    font-size: 64px; font-weight: 500; color: var(--silver);
    display: flex; align-items: center; gap: 16px;
  }
  .wordmark .dot {
    width: 18px; height: 18px; border-radius: 50%;
    background: currentColor;
  }
  .card--back .tagline {
    position: absolute; bottom: 44px; left: 0; right: 0;
    text-align: center; font-size: 15px; letter-spacing: 1.5px;
    color: var(--tagline);
  }
  /* Front side */
  .card--front {
    display: flex; align-items: center;
    padding: 0 40px 0 36px;
  }
  .card--front .brand {
    width: 280px;
    display: flex; justify-content: center;
  }
  .card--front .wordmark {
    font-size: 56px; font-weight: 500; color: var(--green);
    display: flex; align-items: center; gap: 12px;
  }
  .wordmark .dot--yellow { background: var(--yellow); }
  .divider {
    width: 2px; height: 200px; background: var(--green);
    margin: 0 28px 0 20px;
  }
  .person .name {
    font-size: 30px; font-weight: 600; letter-spacing: 2px;
    color: var(--yellow); text-transform: uppercase; line-height: 1.1;
  }
  .person .role {
    font-size: 20px; font-weight: 500; letter-spacing: 1px;
    color: var(--white); margin-bottom: 22px;
  }
  .contacts { list-style: none; }
  .contacts li {
    display: flex; align-items: center; gap: 14px;
    font-size: 18px; letter-spacing: 1.5px; color: var(--white);
    line-height: 1.6; white-space: nowrap;
  }
  .contacts svg { width: 16px; height: 16px; flex: none; }
  .contacts .accent { color: var(--yellow); }
</style>
</head>
<body>
<main class="stage">
  <section class="card card--back" aria-label="Card back">
    <div class="wordmark"><span class="dot"></span>Velmorin</div>
    <p class="tagline">Hacemos más por ti!</p>
  </section>

  <section class="card card--front" aria-label="Card front">
    <div class="brand">
      <div class="wordmark"><span class="dot dot--yellow"></span>Velmorin</div>
    </div>
    <div class="divider"></div>
    <div class="person">
      <h1 class="name">Tomas Brevik</h1>
      <p class="role">Managing Director</p>
      <ul class="contacts">
        <li>
          <svg viewBox="0 0 16 16"><rect x="4" y="1" width="8" height="14" rx="1.5" fill="none" stroke="#f2c21b" stroke-width="1.6"/></svg>
          +61 491058263
        </li>
        <li>
          <svg viewBox="0 0 16 16"><rect x="1" y="3" width="14" height="10" rx="1" fill="#f2c21b"/><path d="M1 4 L8 9 L15 4" fill="none" stroke="#173a5c" stroke-width="1.4"/></svg>
          tomas@velmorin.com.au
        </li>
        <li>
          <svg viewBox="0 0 16 16"><circle cx="6.5" cy="6.5" r="4.5" fill="none" stroke="#f2c21b" stroke-width="2"/><path d="M10 10 L15 15" stroke="#f2c21b" stroke-width="2.4" stroke-linecap="round"/></svg>
          <span>www.<span class="accent">velmorin.com.au</span></span>
        </li>
        <li>
          <svg viewBox="0 0 16 16"><path d="M8 1 C4.7 1 3 3.4 3 6 C3 9.5 8 15 8 15 C8 15 13 9.5 13 6 C13 3.4 11.3 1 8 1 Z" fill="#f2c21b"/><circle cx="8" cy="6" r="2" fill="#173a5c"/></svg>
          Melbourne, Australia
        </li>
      </ul>
    </div>
  </section>
</main>
</body>
</html>
```